General Dental Office Business Card

I run a private general dental office in southern California, and would like a refresh/redesign of my business card. I focus on quality care rather than volume. The email address on the uploaded current card should be updated to: info@marbleshoredental.example. The current card's logo is a deboss, but I am open to other ideas. The logo can be refreshed, but it is something that's been with me since the beginning of the office, so I wouldn't want a drastic redesign.
Target Market(s)
Adults 18-99, whoever needs dental services
Industry/Entity Type
Healthcare/Dental
Contact Information for Business Card
Name, Address, Phone, email
Colors
Designer to choose colors to be used in the design.
Requirements
Must have
- Logo (Same as original one in the uploaded file), space on back for appointment time/date

```html
<!DOCTYPE html>
<html lang="en">
<head>
<meta charset="utf-8">
<title>Marble Shore Dental – Business Card</title>
<link href="https://fonts.googleapis.com/css2?family=Montserrat:wght@600;700&family=Mulish:wght@400;600&display=swap" rel="stylesheet">
<style>
  :root {
    --bg: #d3d3ce;
    --card: #070707;
    --blue: #86d4ec;
    --text: #e9e9e9;
    --muted: #8a8a8a;
  }
  * { box-sizing: border-box; margin: 0; padding: 0; }
  html, body { width: 1200px; height: 801px; overflow: hidden; }
  body {
    background: var(--bg);
    font-family: "Mulish", sans-serif;
    position: relative;
  }
  .card {
    position: absolute;
    top: 246px;
    width: 540px;
    height: 309px;
    background: var(--card);
    overflow: hidden;
    box-shadow: 0 10px 24px rgba(0,0,0,.28);
  }
  .card--front { left: 40px; }
  .card--back { left: 620px; }
  .waves { position: absolute; inset: 0; width: 100%; height: 100%; }

  /* front */
  .logo-mark {
    position: absolute; left: 72px; top: 62px;
    width: 116px; height: 116px; border-radius: 50%;
    background: var(--blue);
  }
  .logo-name {
    position: absolute; left: 30px; top: 196px; width: 200px;
    text-align: center; color: var(--blue);
    font-family: "Montserrat", sans-serif; font-weight: 600;
    font-size: 12px; letter-spacing: 1.5px;
  }
  .divider {
    position: absolute; left: 262px; top: 34px;
    width: 2px; height: 132px; background: var(--blue);
  }
  .contact { position: absolute; left: 282px; top: 26px; color: var(--text); }
  .contact__name {
    font-family: "Montserrat", sans-serif; font-weight: 700;
    color: var(--blue); font-size: 16px; letter-spacing: .3px;
  }
  .contact__role { font-size: 11px; margin-bottom: 8px; }
  .contact__practice { color: var(--blue); font-size: 16px; letter-spacing: .4px; }
  .contact__address { font-size: 10.5px; line-height: 1.3; margin-bottom: 8px; }
  .contact__line { display: flex; align-items: center; gap: 6px; font-size: 10.5px; line-height: 1.45; }
  .contact__line svg { width: 10px; height: 10px; flex: none; }
  .contact__web { color: var(--blue); }

  /* back */
  .back__title {
    position: absolute; left: 34px; top: 24px;
    font-family: "Montserrat", sans-serif; font-weight: 700;
    color: var(--blue); font-size: 20px; letter-spacing: 1px;
  }
  .form { position: absolute; left: 34px; top: 68px; width: 470px; color: var(--text); font-size: 12px; }
  .form__row { display: flex; align-items: flex-end; gap: 6px; height: 21px; }
  .form__row--gap { margin-top: 8px; }
  .form__label { white-space: nowrap; }
  .form__fill { flex: 1; border-bottom: 1.5px dotted var(--blue); margin-bottom: 3px; }
  .form__suffix { white-space: nowrap; }
  .days { display: flex; gap: 20px; margin-top: 14px; font-size: 12px; color: var(--text); }
  .day { display: flex; align-items: center; gap: 3px; }
  .day__box { width: 9px; height: 9px; border: 1.5px solid var(--blue); }
</style>
</head>
<body>

<section class="card card--front" aria-label="Business card front">
  <svg class="waves" viewBox="0 0 540 309" aria-hidden="true">
    <g fill="none" stroke="#86d4ec" stroke-width="7">
      <path d="M-10,300 C120,290 180,268 270,244 C360,220 440,200 550,146"/>
      <path d="M-10,313 C120,303 180,281 270,257 C360,233 440,213 550,159"/>
      <path d="M-10,326 C120,316 180,294 270,270 C360,246 440,226 550,172"/>
      <path d="M-10,339 C120,329 180,307 270,283 C360,259 440,239 550,185"/>
    </g>
  </svg>
  <div class="logo-mark"></div>
  <div class="logo-name">MARBLE SHORE DENTAL</div>
  <div class="divider"></div>
  <div class="contact">
    <p class="contact__name">DANIEL R. MORENO DDS</p>
    <p class="contact__role">General Dentistry</p>
    <p class="contact__practice">Marble Shore Dental</p>
    <p class="contact__address">1820 Coastline Avenue Laguna Vista,<br>CA 92000</p>
    <p class="contact__line">
      <svg viewBox="0 0 10 10"><path d="M2 1 L4 3 L3 4 Q4 6 6 7 L7 6 L9 8 L8 9 Q3 9 1 2 Z" fill="#e9e9e9"/></svg>
      949-555-0142
    </p>
    <p class="contact__line">
      <svg viewBox="0 0 10 10"><rect x="1" y="2" width="8" height="6" fill="none" stroke="#e9e9e9"/><path d="M1 2 L5 5.5 L9 2" fill="none" stroke="#e9e9e9"/></svg>
      info@marbleshoredental.example
    </p>
    <p class="contact__line contact__web">
      <svg viewBox="0 0 10 10"><circle cx="5" cy="5" r="4" fill="none" stroke="#e9e9e9"/><path d="M1 5 H9 M5 1 V9" stroke="#e9e9e9"/></svg>
      www.marbleshoredental.example
    </p>
  </div>
</section>

<section class="card card--back" aria-label="Business card back, appointment form">
  <svg class="waves" viewBox="0 0 540 309" aria-hidden="true">
    <g fill="none" stroke="#86d4ec" stroke-width="7">
      <path d="M-10,262 C120,282 240,232 370,238 C450,242 500,222 550,198"/>
      <path d="M-10,275 C120,295 240,245 370,251 C450,255 500,235 550,211"/>
      <path d="M-10,288 C120,308 240,258 370,264 C450,268 500,248 550,224"/>
      <path d="M-10,301 C120,321 240,271 370,277 C450,281 500,261 550,237"/>
    </g>
  </svg>
  <h2 class="back__title">MARBLE SHORE DENTAL</h2>
  <div class="form">
    <div class="form__row"><span class="form__label">Patient Name :</span><span class="form__fill"></span></div>
    <div class="form__row form__row--gap"><span class="form__label">Appointment Date</span><span class="form__fill"></span><span class="form__suffix">am / pm</span></div>
    <div class="form__row"><span class="form__label">Appointment Date</span><span class="form__fill"></span><span class="form__suffix">am / pm</span></div>
    <div class="form__row form__row--gap"><span class="form__label">Time</span><span class="form__fill"></span></div>
    <div class="form__row"><span class="form__label">Time</span><span class="form__fill"></span></div>
    <div class="days">
      <span class="day">Sun<span class="day__box"></span></span>
      <span class="day">Mon<span class="day__box"></span></span>
      <span class="day">Tue<span class="day__box"></span></span>
      <span class="day">Wed<span class="day__box"></span></span>
      <span class="day">Thu<span class="day__box"></span></span>
      <span class="day">Fri<span class="day__box"></span></span>
      <span class="day">Sat<span class="day__box"></span></span>
    </div>
  </div>
</section>

</body>
</html>
```